Brimforge Services

Hi, im after app that works kind of like a 3 part form:

1.Office submit the job on the app ( customer name. customer address and description of the issue)
2. This then gets sent to the engineers who can see what jobs are available. they can then click on this job and then submit there details (for example how they fixed the issue, what materials have been used.
3. This then get sent back to the office for approval before they sent this to the accounts for invoicing?

is this possible?

Requirements
Must have
• Editable form template.
Mandatory fields

```html
<!DOCTYPE html>
<html lang="en">
<head>
<meta charset="utf-8">
<title>Brimforge Services – Engineer App Screens</title>
<link rel="stylesheet" href="https://fonts.googleapis.com/css2?family=Montserrat:wght@600;700&family=Open+Sans:wght@400;600;700&display=swap">
<style>
:root{
  --bg:#e4e4e4;
  --white:#ffffff;
  --blue:#1a96d8;
  --nav-blue:#0f95dc;
  --green:#72c62a;
  --ink:#2b2b2b;
  --muted:#555a60;
  --line:#cfd3d6;
  --badge:#6f7275;
  --sky-light:#8fcbef;
  --sky-dark:#1a5fae;
  --splash-top:#ffffff;
  --splash-bottom:#d9effb;
  --map:#eceae6;
}
*{box-sizing:border-box;margin:0;padding:0}
html,body{width:1200px;height:584px;overflow:hidden;background:var(--bg)}
body{position:relative;font-family:"Open Sans",Arial,sans-serif;color:var(--ink)}
.screen{position:absolute;top:44px;width:167px;height:361px;background:var(--white);overflow:hidden;box-shadow:0 2px 8px rgba(0,0,0,.06)}
.screen > *{position:absolute}
.splash{left:70px;background:linear-gradient(180deg,var(--splash-top),var(--splash-bottom))}
.login{left:293px}
.home{left:517px}
.form{left:740px;height:501px}
.map-screen{left:963px}

.brand{display:flex;align-items:center;gap:4px;font-weight:700;color:var(--blue);font-size:8px;white-space:nowrap}
.brand-dot{width:9px;height:9px;border-radius:50%;background:var(--blue)}

.eyebrow{font-size:7.5px;color:var(--ink)}
.headline{font-family:"Montserrat",sans-serif;font-weight:700;color:var(--blue);font-size:11px;white-space:nowrap}
.lead{font-size:7.5px;color:var(--muted)}
.label{font-size:7px;font-weight:600;color:var(--muted)}
.value{font-size:7.3px;color:var(--ink);line-height:11.5px}
.rule{height:1px;background:var(--line)}
.icon-end{right:9px;width:9px;height:9px}

.btn{display:flex;align-items:center;justify-content:center;gap:3px;background:var(--green);color:var(--white);border-radius:2px;font-weight:600;white-space:nowrap}
.btn svg{width:7px;height:7px}
.btn-lg{font-size:9px;height:22px}
.link{font-size:7px;color:var(--blue);font-weight:600}

.skyline{background:linear-gradient(180deg,var(--sky-light) 0%,#5aa9e0 55%,var(--sky-dark) 100%)}
.avatar{width:20px;height:20px;border-radius:50%;background:#3d3a38}

.section-title{font-family:"Montserrat",sans-serif;font-weight:700;font-size:9.5px;color:#111}
.job-card{left:9px;width:149px;height:75px;background:var(--white);border-radius:3px;box-shadow:0 1px 4px rgba(0,0,0,.14)}
.job-card > *{position:absolute}
.job-name{left:9px;top:6px;font-family:"Montserrat",sans-serif;font-weight:700;font-size:8.5px;color:var(--blue)}
.badge{display:flex;align-items:center;gap:2px;background:var(--badge);color:var(--white);font-size:5px;border-radius:6px;height:10px;padding:0 5px 0 4px;white-space:nowrap}
.badge svg{width:5px;height:5px}
.job-card .badge{right:8px;top:6px}
.job-desc{left:9px;top:21px;width:134px;font-size:7px;line-height:10.7px;color:var(--ink)}
.job-card .rule{left:9px;right:9px;top:47px}
.job-actions{left:8px;top:55px;display:flex;gap:4.5px}
.job-actions .btn{width:41px;height:13px;font-size:6.5px;font-weight:400}

.nav{left:0;width:167px;height:31px;background:var(--nav-blue);display:flex;align-items:center;justify-content:space-around;padding:0 4px}
.nav-item{display:flex;flex-direction:column;align-items:center;color:var(--white);font-size:6.5px;font-weight:600;width:30px}
.nav-item svg{width:10px;height:10px}

.back{left:9px;top:9px;width:11px;height:7px}
.browse{left:9px;top:351px;width:37px;height:14px;background:var(--badge);color:var(--white);font-size:6.5px;display:flex;align-items:center;justify-content:center;border-radius:1px}
.hint{font-size:5.7px;color:var(--muted)}
.map-area{left:0;top:40px;width:167px;height:155px;background:var(--map)}
</style>
</head>
<body>

<!-- Splash -->
<section class="screen splash" aria-label="Splash screen">
  <div class="brand" style="left:41px;top:176px;font-size:10px"><span class="brand-dot" style="width:11px;height:11px"></span>Brimforge Services</div>
</section>

<!-- Login -->
<section class="screen login" aria-label="Login screen">
  <div class="brand" style="left:9px;top:18px">  <span class="brand-dot"></span>Brimforge Services</div>
  <p class="eyebrow" style="left:9px;top:76px;font-size:9.5px">Hello,</p>
  <h1 class="headline" style="left:9px;top:88px">Welcome Back!</h1>
  <p class="lead" style="left:9px;top:107px">Enter your credentials to login</p>

  <p class="label" style="left:9px;top:139px">Email</p>
  <p class="value" style="left:9px;top:154px">johndoe@example.com</p>
  <svg class="icon-end" style="top:155px" viewBox="0 0 10 10"><rect x="1" y="2" width="8" height="6" fill="none" stroke="#444" stroke-width="1"/><path d="M1 2l4 3.5L9 2" fill="none" stroke="#444" stroke-width="1"/></svg>
  <div class="rule" style="left:9px;right:9px;top:168px"></div>

  <p class="label" style="left:9px;top:178px">Password</p>
  <p class="value" style="left:9px;top:192px;letter-spacing:.5px">..............</p>
  <svg class="icon-end" style="top:194px" viewBox="0 0 10 10"><rect x="2" y="4.5" width="6" height="5" fill="#444"/><path d="M3.3 4.5V3a1.7 1.7 0 0 1 3.4 0v1.5" fill="none" stroke="#444" stroke-width="1"/></svg>
  <div class="rule" style="left:9px;right:9px;top:207px"></div>

  <svg style="left:9px;top:217px;width:10px;height:10px" viewBox="0 0 10 10"><rect x=".5" y=".5" width="9" height="9" fill="none" stroke="#999"/><path d="M2 5l2 2 4-5" fill="none" stroke="#333" stroke-width="1.3"/></svg>
  <p class="value" style="left:26px;top:216px">Remember Me</p>

  <div class="btn btn-lg" style="left:9px;top:236px;width:149px">Sign In</div>
  <svg style="left:138px;top:244px;width:12px;height:6px" viewBox="0 0 12 6"><path d="M0 3h11M8 .5L11 3 8 5.5" fill="none" stroke="#fff" stroke-width="1"/></svg>
  <p class="link" style="left:0;width:167px;text-align:center;top:266px">Forgot Password?</p>

  <div class="skyline" role="img" aria-label="City skyline illustration in blue tones" style="left:0;top:310px;width:167px;height:51px"></div>
</section>

<!-- Home / job list -->
<section class="screen home" aria-label="Jobs list screen">
  <p class="eyebrow" style="left:9px;top:10px;font-size:7px">Good Morning,</p>
  <h1 class="headline" style="left:9px;top:20px;font-size:10.5px">John Doe!</h1>
  <div class="avatar" role="img" aria-label="Engineer profile photo" style="left:139px;top:11px"></div>
  <div class="skyline" role="img" aria-label="City skyline illustration in blue tones" style="left:0;top:40px;width:167px;height:46px"></div>

  <h2 class="section-title" style="left:9px;top:94px">Your Jobs</h2>
  <p class="link" style="left:92px;top:96px;font-weight:400">Completed Jobs</p>
  <svg style="left:149px;top:99px;width:9px;height:5px" viewBox="0 0 9 5"><path d="M0 2.5h8M6 .5l2 2-2 2" fill="none" stroke="#1a96d8" stroke-width=".9"/></svg>

  <article class="job-card" style="top:113px">
    <h3 class="job-name">Owen Hartley</h3>
    <span class="badge"><svg viewBox="0 0 6 6"><path d="M3 6C1 3.6.8 2.9.8 2.2a2.2 2.2 0 0 1 4.4 0c0 .7-.2 1.4-2.2 3.8z" fill="#fff"/></svg>2.5 Miles</span>
    <p class="job-desc">Installation, Repair and Maintenance of Septic Tanks, Sewage Treatment...</p>
    <div class="rule"></div>
    <div class="job-actions">
      <span class="btn"><svg viewBox="0 0 8 8"><path d="M1.5 .5l1.5 1.6-.8 1a5 5 0 0 0 2.7 2.7l1-.8L7.5 6.5 6.5 7.5C3.5 7.5.5 4.5.5 1.5z" fill="#fff"/></svg>Call</span>
      <span class="btn"><svg viewBox="0 0 8 8"><path d="M4 .8c2 0 3.5 1.2 3.5 2.8S6 6.4 4 6.4l-2.4 1 .5-1.5C1 5.4.5 4.6.5 3.6.5 2 2 .8 4 .8z" fill="#fff"/></svg>Chat</span>
      <span class="btn"><svg viewBox="0 0 8 8"><path d="M4 7.5C2 5 1.5 4 1.5 3a2.5 2.5 0 0 1 5 0c0 1-.5 2-2.5 4.5z" fill="#fff"/></svg>Map</span>
    </div>
  </article>

  <article class="job-card" style="top:198px">
    <h3 class="job-name">Leo Brandt</h3>
    <span class="badge"><svg viewBox="0 0 6 6"><path d="M3 6C1 3.6.8 2.9.8 2.2a2.2 2.2 0 0 1 4.4 0c0 .7-.2 1.4-2.2 3.8z" fill="#fff"/></svg>5.3 Miles</span>
    <p class="job-desc">Jet Vac Cleaning Service for Drains, Sewers, Interceptors, Septic Tanks...</p>
    <div class="rule"></div>
    <div class="job-actions">
      <span class="btn"><svg viewBox="0 0 8 8"><path d="M1.5 .5l1.5 1.6-.8 1a5 5 0 0 0 2.7 2.7l1-.8L7.5 6.5 6.5 7.5C3.5 7.5.5 4.5.5 1.5z" fill="#fff"/></svg>Call</span>
      <span class="btn"><svg viewBox="0 0 8 8"><path d="M4 .8c2 0 3.5 1.2 3.5 2.8S6 6.4 4 6.4l-2.4 1 .5-1.5C1 5.4.5 4.6.5 3.6.5 2 2 .8 4 .8z" fill="#fff"/></svg>Chat</span>
      <span class="btn"><svg viewBox="0 0 8 8"><path d="M4 7.5C2 5 1.5 4 1.5 3a2.5 2.5 0 0 1 5 0c0 1-.5 2-2.5 4.5z" fill="#fff"/></svg>Map</span>
    </div>
  </article>

  <article class="job-card" style="top:283px">
    <h3 class="job-name">Miles Carver</h3>
    <span class="badge"><svg viewBox="0 0 6 6"><path d="M3 6C1 3.6.8 2.9.8 2.2a2.2 2.2 0 0 1 4.4 0c0 .7-.2 1.4-2.2 3.8z" fill="#fff"/></svg>6.2 Miles</span>
    <p class="job-desc">Sewage Treatment Plants, Pumps, Pump Stations, Interceptors...</p>
  </article>

  <nav class="nav" style="top:330px">
    <span class="nav-item"><svg viewBox="0 0 10 10"><path d="M5 1L1 4.5V9h3V6.5h2V9h3V4.5z" fill="#fff"/></svg>Home</span>
    <span class="nav-item"><svg viewBox="0 0 10 10"><circle cx="4.3" cy="4.3" r="3" fill="none" stroke="#fff" stroke-width="1.2"/><path d="M6.5 6.5L9 9" stroke="#fff" stroke-width="1.3"/></svg></span>
    <span class="nav-item"><svg viewBox="0 0 10 10"><path d="M5 1.5a2.8 2.8 0 0 1 2.8 2.8V7l1 1H1.2l1-1V4.3A2.8 2.8 0 0 1 5 1.5zM4 8.6h2a1 1 0 0 1-2 0z" fill="#fff"/><circle cx="7.8" cy="2" r="1.5" fill="#fff"/></svg></span>
    <span class="nav-item"><svg viewBox="0 0 10 10"><path d="M1 2.5h8M1 5h8M1 7.5h8" stroke="#fff" stroke-width=".9"/><circle cx="6.5" cy="2.5" r="1" fill="#0f95dc" stroke="#fff" stroke-width=".8"/><circle cx="3.5" cy="5" r="1" fill="#0f95dc" stroke="#fff" stroke-width=".8"/><circle cx="6" cy="7.5" r="1" fill="#0f95dc" stroke="#fff" stroke-width=".8"/></svg></span>
  </nav>
</section>

<!-- Job completion form -->
<section class="screen form" aria-label="Job details form screen">
  <svg class="back" viewBox="0 0 11 7"><path d="M11 3.5H1M3.5 1L1 3.5 3.5 6" fill="none" stroke="#1a96d8" stroke-width="1"/></svg>
  <h1 class="headline" style="left:9px;top:21px">Fill up the form details</h1>
  <div class="avatar" role="img" aria-label="Engineer profile photo" style="left:139px;top:11px"></div>
  <p class="lead" style="left:9px;top:38px">Enter below details of the job</p>

  <p class="label" style="left:9px;top:60px">Name</p>
  <p class="value" style="left:9px;top:74px">Owen Hartley</p>
  <div class="rule" style="left:9px;right:9px;top:88px"></div>

  <p class="label" style="left:9px;top:97px">Email</p>
  <p class="value" style="left:9px;top:111px">owen.hartley@example.com</p>
  <div class="rule" style="left:9px;right:9px;top:125px"></div>

  <p class="label" style="left:9px;top:135px">Phone Number</p>
  <p class="value" style="left:9px;top:149px">+44 100 200 300 4</p>
  <div class="rule" style="left:9px;right:9px;top:163px"></div>

  <p class="label" style="left:9px;top:173px">Address</p>
  <p class="value" style="left:9px;top:187px">14 Fernvale Road, Leeds, UK, 9LTX</p>
  <div class="rule" style="left:9px;right:9px;top:201px"></div>

  <p class="label" style="left:9px;top:210px">Start Date</p>
  <p class="value" style="left:9px;top:224px">12/13/2020</p>
  <svg style="left:69px;top:225px;width:9px;height:9px" viewBox="0 0 9 9"><rect x=".5" y="1.5" width="8" height="7" fill="none" stroke="#555"/><path d="M.5 3.5h8M2.5 0v2.5M6.5 0v2.5M2 5h1M4 5h1M6 5h1M2 7h1M4 7h1M6 7h1" stroke="#555" stroke-width=".8"/></svg>
  <div class="rule" style="left:9px;width:71px;top:238px"></div>
  <p class="label" style="left:89px;top:210px">End Date</p>
  <p class="value" style="left:89px;top:224px">12/13/2020</p>
  <svg style="left:149px;top:225px;width:9px;height:9px" viewBox="0 0 9 9"><rect x=".5" y="1.5" width="8" height="7" fill="none" stroke="#555"/><path d="M.5 3.5h8M2.5 0v2.5M6.5 0v2.5M2 5h1M4 5h1M6 5h1M2 7h1M4 7h1M6 7h1" stroke="#555" stroke-width=".8"/></svg>
  <div class="rule" style="left:89px;right:9px;top:238px"></div>

  <p class="label" style="left:9px;top:248px">Time Taken for Job Completion</p>
  <p class="value" style="left:9px;top:262px">5</p>
  <div class="rule" style="left:9px;width:45px;top:276px"></div>
  <p class="value" style="left:60px;top:261px">(In Hours)</p>

  <p class="label" style="left:9px;top:285px">Job Description</p>
  <p class="value" style="left:9px;top:300px;width:148px">Installation, Repair and Maintenance of Septic Tanks, Sewage Treatment</p>
  <div class="rule" style="left:9px;right:9px;top:327px"></div>

  <p class="label" style="left:9px;top:337px">Attachment</p>
  <span class="browse">Browse</span>
  <p class="value" style="left:52px;top:352px">File Name</p>
  <div class="rule" style="left:9px;right:9px;top:366px"></div>
  <p class="hint" style="left:9px;top:369px">Upload file in .jpg, .gif, .png, .pdf format</p>

  <p class="label" style="left:9px;top:386px">Comments</p>
  <p class="value" style="left:9px;top:400px;width:140px">Lorem Ipsum is simply dummy text of the printing and typesetting industry.</p>
  <div class="rule" style="left:9px;right:9px;top:428px"></div>

  <div class="btn btn-lg" style="left:9px;top:437px;width:149px;height:23px">Submit for Approval</div>

  <nav class="nav" style="top:470px">
    <span class="nav-item"><svg viewBox="0 0 10 10"><path d="M5 1L1 4.5V9h3V6.5h2V9h3V4.5z" fill="#fff"/></svg></span>
    <span class="nav-item"><svg viewBox="0 0 10 10"><circle cx="4.3" cy="4.3" r="3" fill="none" stroke="#fff" stroke-width="1.2"/><path d="M6.5 6.5L9 9" stroke="#fff" stroke-width="1.3"/></svg></span>
    <span class="nav-item"><svg viewBox="0 0 10 10"><path d="M5 1.5a2.8 2.8 0 0 1 2.8 2.8V7l1 1H1.2l1-1V4.3A2.8 2.8 0 0 1 5 1.5zM4 8.6h2a1 1 0 0 1-2 0z" fill="#fff"/><circle cx="7.8" cy="2" r="1.5" fill="#fff"/></svg></span>
    <span class="nav-item"><svg viewBox="0 0 10 10"><path d="M1 2.5h8M1 5h8M1 7.5h8" stroke="#fff" stroke-width=".9"/><circle cx="6.5" cy="2.5" r="1" fill="#0f95dc" stroke="#fff" stroke-width=".8"/><circle cx="3.5" cy="5" r="1" fill="#0f95dc" stroke="#fff" stroke-width=".8"/><circle cx="6" cy="7.5" r="1" fill="#0f95dc" stroke="#fff" stroke-width=".8"/></svg></span>
  </nav>
</section>

<!-- Map / job location -->
<section class="screen map-screen" aria-label="Job location screen">
  <svg class="back" viewBox="0 0 11 7"><path d="M11 3.5H1M3.5 1L1 3.5 3.5 6" fill="none" stroke="#1a96d8" stroke-width="1"/></svg>
  <h1 class="headline" style="left:9px;top:21px">Map</h1>
  <div class="avatar" role="img" aria-label="Engineer profile photo" style="left:139px;top:11px"></div>
  <div class="map-area" role="img" aria-label="Street map showing route from current location to the job address"></div>

  <h2 class="section-title" style="left:10px;top:205px;font-size:8.5px">Owen Hartley</h2>
  <span class="badge" style="right:9px;top:205px"><svg viewBox="0 0 6 6"><path d="M3 6C1 3.6.8 2.9.8 2.2a2.2 2.2 0 0 1 4.4 0c0 .7-.2 1.4-2.2 3.8z" fill="#fff"/></svg>2.5 Miles</span>
  <p class="value" style="left:10px;top:223px">14 Fernvale Road, Leeds, UK, 9LTX</p>
  <div class="rule" style="left:10px;right:9px;top:241px"></div>

  <p class="label" style="left:10px;top:248px">Job Description</p>
  <p class="value" style="left:10px;top:263px;width:135px">Installation, Repair and Maintenance of Septic Tanks, Sewage Treatment</p>

  <div class="btn" style="left:10px;top:295px;width:70px;height:20px;font-size:8.5px"><svg viewBox="0 0 8 8" style="width:8px;height:8px"><path d="M1.5 .5l1.5 1.6-.8 1a5 5 0 0 0 2.7 2.7l1-.8L7.5 6.5 6.5 7.5C3.5 7.5.5 4.5.5 1.5z" fill="#fff"/></svg>Call</div>
  <div class="btn" style="left:88px;top:295px;width:70px;height:20px;font-size:8.5px"><svg viewBox="0 0 8 8" style="width:8px;height:8px"><path d="M4 .8c2 0 3.5 1.2 3.5 2.8S6 6.4 4 6.4l-2.4 1 .5-1.5C1 5.4.5 4.6.5 3.6.5 2 2 .8 4 .8z" fill="#fff"/></svg>Chat</div>

  <nav class="nav" style="top:330px">
    <span class="nav-item"><svg viewBox="0 0 10 10"><path d="M5 1L1 4.5V9h3V6.5h2V9h3V4.5z" fill="#fff"/></svg></span>
    <span class="nav-item"><svg viewBox="0 0 10 10"><circle cx="4.3" cy="4.3" r="3" fill="none" stroke="#fff" stroke-width="1.2"/><path d="M6.5 6.5L9 9" stroke="#fff" stroke-width="1.3"/></svg></span>
    <span class="nav-item"><svg viewBox="0 0 10 10"><path d="M5 1.5a2.8 2.8 0 0 1 2.8 2.8V7l1 1H1.2l1-1V4.3A2.8 2.8 0 0 1 5 1.5zM4 8.6h2a1 1 0 0 1-2 0z" fill="#fff"/><circle cx="7.8" cy="2" r="1.5" fill="#fff"/></svg></span>
    <span class="nav-item"><svg viewBox="0 0 10 10"><path d="M1 2.5h8M1 5h8M1 7.5h8" stroke="#fff" stroke-width=".9"/><circle cx="6.5" cy="2.5" r="1" fill="#0f95dc" stroke="#fff" stroke-width=".8"/><circle cx="3.5" cy="5" r="1" fill="#0f95dc" stroke="#fff" stroke-width=".8"/><circle cx="6" cy="7.5" r="1" fill="#0f95dc" stroke="#fff" stroke-width=".8"/></svg></span>
  </nav>
</section>

</body>
</html>
```